Glidewell Depot logo

Glidewell Depot is owned and operated by industry professionals with years of direct experience in providing customers with the right equipment to suit their needs. Our specialty lies within dealing in the Halvern Medical range of products. Our product range is suited to both the new user and for those that know what they want, a full line of products ranging from ultra-light wheelchairs, wheelchairs for sport and recreation and paediatric or just everyday use.

Industry/Entity Type

Recreation

Contact Information for Business Card

name, title, landline,fax,mobile,email,web address,physical address,logo,possibly a wheelchair pic

Requirements
Must have
• logo - uploaded
Nice to have
• colour scheme consistent with
www.glidewelldepot.com.au

```html
<!DOCTYPE html>
<html lang="en">
<head>
<meta charset="utf-8">
<title>Glidewell Depot – Business Card</title>
<link href="https://fonts.googleapis.com/css2?family=Arimo:wght@400;700&display=swap" rel="stylesheet">
<style>
  :root {
    --page-bg: #ecebea;
    --card-bg: #ffffff;
    --card-edge: #d9d9d9;
    --plum: #4b1446;
    --ocean: #17668f;
    --chair-light: #e9ecee;
    --chair-mid: #d3d9dc;
    --chair-accent: #e4ecd6;
  }
  * { margin: 0; padding: 0; box-sizing: border-box; }
  html, body {
    width: 1200px;
    height: 1000px;
    overflow: hidden;
    background: var(--page-bg);
    font-family: "Arimo", Arial, sans-serif;
  }
  .card {
    position: absolute;
    left: 80px;
    top: 217px;
    width: 1040px;
    height: 565px;
    background: var(--card-bg);
    border: 2px solid var(--card-edge);
    border-radius: 39px;
    overflow: hidden;
  }
  .card__chair-photo {
    position: absolute;
    left: 254px;
    top: 9px;
    width: 527px;
    height: 549px;
    border-radius: 40px;
    background:
      radial-gradient(ellipse at 35% 60%, var(--chair-mid) 0%, transparent 55%),
      radial-gradient(ellipse at 70% 55%, var(--chair-accent) 0%, transparent 50%),
      linear-gradient(180deg, var(--chair-light), #f4f6f7);
    opacity: 0.85;
  }
  .brand-mark {
    position: absolute;
    left: 760px;
    top: 40px;
    width: 248px;
    display: flex;
    flex-direction: column;
    align-items: center;
  }
  .brand-mark__row {
    display: flex;
    align-items: center;
    gap: 10px;
    margin-top: 40px;
  }
  .brand-mark__dot {
    width: 34px;
    height: 34px;
    border-radius: 50%;
    background: var(--ocean);
  }
  .brand-mark__name {
    color: var(--plum);
    font-weight: 700;
    font-size: 27px;
    line-height: 1.1;
    white-space: nowrap;
  }
  .brand-mark__tagline {
    margin-top: 82px;
    color: var(--ocean);
    font-weight: 700;
    font-size: 12px;
    white-space: nowrap;
  }
  .card__title {
    position: absolute;
    left: 40px;
    top: 218px;
    color: var(--plum);
    font-size: 96px;
    font-weight: 400;
    line-height: 1;
    white-space: nowrap;
  }
  .card__tagline {
    position: absolute;
    left: 55px;
    top: 315px;
    color: var(--ocean);
    font-size: 25px;
    letter-spacing: 0.44em;
    white-space: nowrap;
  }
  .contact-list {
    position: absolute;
    left: 113px;
    top: 373px;
    list-style: none;
    color: var(--plum);
    font-size: 19px;
  }
  .contact-list li { height: 47px; line-height: 24px; }
  .card__web {
    position: absolute;
    right: 34px;
    top: 505px;
    color: var(--ocean);
    font-size: 26px;
    white-space: nowrap;
  }
</style>
</head>
<body>
  <section class="card">
    <div class="card__chair-photo" role="img" aria-label="Faded photo of a lightweight sport wheelchair with green frame"></div>

    <div class="brand-mark">
      <div class="brand-mark__row">
        <span class="brand-mark__dot"></span>
        <span class="brand-mark__name">Glidewell Depot</span>
      </div>
      <div class="brand-mark__tagline">SERVICE - KNOWLEDGE - INNOVATION</div>
    </div>

    <h1 class="card__title">Glidewell Depot</h1>
    <p class="card__tagline">SERVICE - KNOWLEDGE - INNOVATION</p>

    <ul class="contact-list">
      <li>Address: Unit 8 14 Fern Street, MARSDEN</li>
      <li>Email: info@glidewelldepot.com.au</li>
      <li>Mobile Number: +61 400 555 182</li>
      <li>Fax Number: +61 2 9000 4821</li>
    </ul>

    <p class="card__web">http://www.glidewelldepot.com.au/</p>
  </section>
</body>
</html>
```